Rock band business card design

I need an edgy double sided business card to hand out at music events and to send out to radio.

It needs to display our logo, web address and social media icons (linkora, plumbit, vostramesh).

Colour scheme to match our website (www.thedrelliq.com)

Please include this quote:
The clock is turning... a reckoning... THE DRELLIQ.

Logo files have been attached.

I look forward to seeing your designs!

Target Market(s)

radio stations, music fans.

Industry/Entity Type

Events

Requirements
Must have
• Website address, social media icons, quote, colour scheme to match www.thedrelliq.com

```html
<!DOCTYPE html>
<html lang="en">
<head>
<meta charset="utf-8">
<title>The Drelliq – Business Card</title>
<link rel="stylesheet" href="https://fonts.googleapis.com/css2?family=Cinzel:wght@700&family=Oswald:wght@600&display=swap">
<style>
  :root {
    --page: #e4e2de;
    --desert-light: #f2c877;
    --desert-mid: #d48a3a;
    --desert-deep: #8a4514;
    --desert-dust: #5a2d10;
    --paper: #f1efea;
    --ink: #141210;
    --accent-red: #d3141b;
    --white: #ffffff;
  }
  * { box-sizing: border-box; margin: 0; padding: 0; }
  html, body { width: 1200px; height: 918px; overflow: hidden; }
  body {
    background: var(--page);
    display: flex;
    flex-direction: column;
    align-items: center;
    justify-content: center;
    gap: 30px;
  }
  .card {
    position: relative;
    width: 700px;
    height: 400px;
    overflow: hidden;
    box-shadow: 0 4px 14px rgba(0,0,0,.18);
  }
  .desert-scene {
    position: absolute;
    inset: 0;
    background:
      radial-gradient(ellipse at 70% 30%, var(--desert-light) 0%, rgba(242,200,119,0) 55%),
      linear-gradient(180deg, var(--desert-light) 0%, var(--desert-mid) 45%, var(--desert-deep) 80%, var(--desert-dust) 100%);
  }

  /* Front */
  .quote {
    position: absolute;
    font-family: "Oswald", sans-serif;
    font-weight: 600;
    text-transform: uppercase;
    color: var(--ink);
    line-height: 1.05;
    letter-spacing: 1px;
  }
  .quote-opening { left: 44px; top: 58px; font-size: 30px; }
  .quote-closing { right: 52px; bottom: 60px; font-size: 30px; text-align: right; }
  .band-name-front {
    position: absolute;
    left: 0; right: 0; top: 160px;
    text-align: center;
    font-family: "Cinzel", serif;
    font-weight: 700;
    font-size: 40px;
    color: var(--ink);
  }

  /* Back */
  .paper-panel { position: absolute; inset: 0; }
  .web-address {
    position: absolute;
    left: 190px; top: 40px;
    width: 440px;
    text-align: center;
    font-family: "Cinzel", serif;
    font-weight: 700;
    color: var(--ink);
    white-space: nowrap;
  }
  .web-address .affix { font-family: "Oswald", sans-serif; font-size: 18px; }
  .web-address .name { font-size: 40px; margin: 0 6px; }
  .band-name-back {
    position: absolute;
    left: 190px; top: 165px;
    width: 440px;
    text-align: center;
    font-family: "Cinzel", serif;
    font-weight: 700;
    font-size: 34px;
    color: var(--ink);
  }
  .social {
    position: absolute;
    font-family: "Oswald", sans-serif;
    font-weight: 600;
    text-transform: uppercase;
    font-size: 22px;
    letter-spacing: .5px;
  }
  .social-linkora { left: 40px; bottom: 60px; color: var(--white); }
  .social-plumbit { right: 40px; bottom: 24px; color: var(--white); }
  .social-vostramesh {
    left: 300px; bottom: 22px;
    color: var(--ink);
    display: flex; align-items: center; gap: 10px;
  }
  .social-vostramesh .dot {
    width: 16px; height: 16px; border-radius: 50%;
    background: var(--accent-red);
  }
</style>
</head>
<body>

  <section class="card card-front">
    <div class="desert-scene" role="img" aria-label="Photograph of desert pyramids under a large rising sun in warm amber haze"></div>
    <p class="quote quote-opening">The clock<br>is turning...</p>
    <p class="band-name-front">THE DRELLIQ</p>
    <p class="quote quote-closing">A reckoning...<br>The Drelliq.</p>
  </section>

  <section class="card card-back">
    <div class="desert-scene" role="img" aria-label="Photograph of desert pyramids in golden light"></div>
    <svg class="paper-panel" width="700" height="400" viewBox="0 0 700 400" aria-hidden="true">
      <polygon points="110,0 700,0 700,110 470,400 280,400" fill="var(--paper)"/>
    </svg>
    <p class="web-address"><span class="affix">www.</span><span class="name">THE DRELLIQ</span><span class="affix">.com</span></p>
    <p class="band-name-back">THE DRELLIQ</p>
    <p class="social social-linkora">linkora</p>
    <p class="social social-vostramesh"><span class="dot"></span>vostramesh</p>
    <p class="social social-plumbit">plumbit</p>
  </section>

</body>
</html>
```